Korvel Tanu Marketing Sdn Bhd needs a handmade soap packaging design

A pure natural material & handmade soap packaging design is needed from a new company called "Korvel Tanu Marketing Sdn Bhd". Soap is specially formulated for sensitive skin patients. Saop contains sacha inchi enzymes, sacha inchi oil, and traditional herbs. All materials are natural. Sacha Inchi is a fruit originated from South America, Peru. Currently widely promoting in Malaysia, contains Omega3, 6 & 9, & vitamin A & E.

Packaging size:
-100mm(length) x 95mm(width), landscape layout.
-hard cover package

Basic Requirement:
-Bring out a FRESH and NATURAL feeling design.
-Sample picture will be attached for reference purpose.
-Company logo is required to be include in design.
-Fruit pictures are for reference only, can change for better one follow designers' idea.
-Omega-3,6 & 9 must include in design.

Industry/Entity Type

It Company

Colors

Designer to choose colors to be used in the design.

Requirements
Must have
• -company logo
• -omega 3,6 & 9
• -Fresh & natural feeling
• -Sacha Inchi fruit picture
Nice to have
• -little creativity from the designers

```html
<!DOCTYPE html>
<html lang="en">
<head>
<meta charset="utf-8">
<title>Korvel Tanu Marketing – Handmade Soap Box Front</title>
<link rel="stylesheet" href="https://fonts.googleapis.com/css2?family=Open+Sans:wght@400;600;700&family=Poppins:wght@600&family=Questrial&display=swap">
<style>
  :root {
    --page-bg: #ececec;
    --kraft: #d6bd9e;
    --kraft-deep: #cbb08f;
    --leaf-green: #5b9a2c;
    --leaf-light: #8cc150;
    --leaf-dark: #3f7a1c;
    --ink: #3a3832;
    --window: #a9998a;
  }
  * { margin: 0; padding: 0; box-sizing: border-box; }
  html, body {
    width: 1200px;
    height: 1200px;
    overflow: hidden;
    background: var(--page-bg);
  }
  .box-front {
    position: absolute;
    left: 100px;
    top: 125px;
    width: 1000px;
    height: 950px;
    background: radial-gradient(ellipse at 60% 45%, var(--kraft) 0%, var(--kraft-deep) 100%);
    overflow: hidden;
    font-family: "Open Sans", sans-serif;
    color: var(--ink);
  }
  .fruit-photo {
    position: absolute;
    left: 0;
    top: 0;
    width: 590px;
    height: 640px;
    border-bottom-right-radius: 70% 60%;
    background:
      radial-gradient(ellipse at 30% 30%, var(--leaf-light) 0%, var(--leaf-green) 45%, rgba(91,154,44,0.55) 75%, rgba(91,154,44,0) 100%);
  }
  .brand-mark {
    position: absolute;
    left: 672px;
    top: 40px;
    width: 150px;
    height: 150px;
    border-radius: 50%;
    background: var(--leaf-green);
  }
  .brand-name {
    position: absolute;
    left: 567px;
    top: 296px;
    width: 360px;
    text-align: center;
    font-family: "Open Sans", sans-serif;
    font-weight: 400;
    font-size: 28px;
    line-height: 36px;
    color: var(--ink);
  }
  .badge {
    position: absolute;
    width: 110px;
    height: 110px;
    border: 4px solid var(--leaf-green);
    border-radius: 50%;
    display: flex;
    flex-direction: column;
    align-items: center;
    justify-content: center;
    color: var(--leaf-dark);
    font-family: "Open Sans", sans-serif;
    line-height: 1.1;
  }
  .badge-label { font-size: 18px; font-weight: 400; }
  .badge-value { font-size: 24px; font-weight: 700; }
  .badge--omega { left: 551px; top: 392px; }
  .badge--vitamin { left: 823px; top: 392px; }
  .soap-window {
    position: absolute;
    left: 603px;
    top: 388px;
    width: 288px;
    height: 416px;
  }
  .tagline {
    position: absolute;
    left: 80px;
    top: 655px;
    font-size: 31px;
    font-weight: 400;
    color: var(--ink);
    white-space: nowrap;
  }
  .tagline strong { font-weight: 700; color: var(--leaf-green); }
  .title-handmade {
    position: absolute;
    left: 70px;
    top: 700px;
    font-family: "Questrial", sans-serif;
    font-weight: 400;
    font-size: 74px;
    line-height: 1;
    color: var(--ink);
  }
  .title-soap {
    position: absolute;
    left: 66px;
    top: 734px;
    font-family: "Poppins", sans-serif;
    font-weight: 600;
    font-size: 146px;
    line-height: 1;
    letter-spacing: -2px;
    color: var(--leaf-green);
  }
  .soap-drip {
    position: absolute;
    left: 340px;
    top: 893px;
    width: 24px;
    height: 36px;
  }
  .care-note {
    position: absolute;
    left: 528px;
    top: 826px;
    display: flex;
    align-items: center;
    gap: 26px;
  }
  .care-icon { width: 84px; height: 56px; }
  .care-text {
    font-size: 28px;
    line-height: 40px;
    color: var(--ink);
  }
  .care-text strong { font-weight: 700; }
</style>
</head>
<body>
  <main class="box-front">
    <div class="fruit-photo" role="img" aria-label="Photo of a green star-shaped sacha inchi fruit with its leaves"></div>

    <div class="brand-mark"></div>
    <p class="brand-name">Korvel Tanu<br>Marketing</p>

    <svg class="soap-window" viewBox="0 0 288 416" aria-hidden="true">
      <path d="M144 0 C 170 80 288 185 288 285 C 288 358 224 416 144 416 C 64 416 0 358 0 285 C 0 185 118 80 144 0 Z" fill="var(--window)"/>
    </svg>

    <div class="badge badge--omega">
      <span class="badge-label">Omega</span>
      <span class="badge-value">3-6-9</span>
    </div>
    <div class="badge badge--vitamin">
      <span class="badge-label">Vitamin</span>
      <span class="badge-value">A&amp;E</span>
    </div>

    <p class="tagline">A pure <strong>natural material</strong></p>
    <h1 class="title-handmade">handmade</h1>
    <p class="title-soap">soap</p>
    <svg class="soap-drip" viewBox="0 0 24 36" aria-hidden="true">
      <path d="M12 0 C 14 10 24 18 24 24 C 24 31 18 36 12 36 C 6 36 0 31 0 24 C 0 18 10 10 12 0 Z" fill="var(--leaf-green)"/>
    </svg>

    <div class="care-note">
      <svg class="care-icon" viewBox="0 0 84 56" aria-hidden="true">
        <path d="M44 2 C 58 4 62 16 54 26 C 42 24 38 12 44 2 Z" fill="var(--leaf-green)"/>
        <path d="M4 36 C 20 32 30 36 40 40 L 58 40 C 63 40 63 46 58 46 L 40 46 M40 46 L 62 46 L 78 35 C 81 33 78 29 74 31 L 60 39" fill="none" stroke="var(--leaf-green)" stroke-width="4" stroke-linecap="round" stroke-linejoin="round"/>
        <path d="M4 52 C 20 48 32 52 46 52 L 60 52" fill="none" stroke="var(--leaf-green)" stroke-width="4" stroke-linecap="round"/>
      </svg>
      <p class="care-text">Specially made<br>for <strong>sensitive</strong> skin</p>
    </div>
  </main>
</body>
</html>
```